Group of 4 companies needs a new brochure.

We need a brochure design for a group of 4 companies that basically offer financial services based in Dubai, UAE. The 4 companies are 1) debt collection 2) auditing and accounting 3) arbitration and legal experts 4) real estate management. We have old content that could guide you and we want each company in the group to be a standalone A4 brochure with all 4 going in a sleeve. Design for all 4 needs to be uniform, going with our logos colors and i would like it to have a modern arabesque feel something modern and geometric but with a hint of arabesque. I want it to position us as a modern innovative company that people want to be associated with. One logo is attached to give an idea of our colors.
Update 1: The Logos and Profiles content have been uploaded please use www.velmo-grp.ae as a reference or for further content.
Please do not include the entire content i uploaded, summarize the important bits.
Update 2: You can join Velmo auditing and Velmo financial consultancy as one brouchure as they have similar activities
If you have any questions do not hesitate to ask!
All the files have been uploaded, if you have any questions do not hesitate to ask!
1. The budget has been increased!
2. You can use our website www.velmo-grp.ae for more information including contacts, location and more information you may need on our operations.
Dear Designers,
There is some confusion regarding the requirements, to clarify, i have posted an image of the folder/brochure to give you an idea of what to do.
Requirement:
1) 1 A4 Folder- Velmo Group logo and contacts/location to put brochures in (see the uploaded picture for an idea of what the folder should look like)
2) 1 A4 Brochure - Velmo Debt Collection
3) 1 A4 Brochure - Velmo Financial Consultants and Velmo Auditing
4) 1 A4 Brochure - Velmo Real Estate Brokers
Further, i will be monitoring the submissions and your comments and i am willing to double the budget if i see the requirements are being met.
Do not hesitate to contact me for any further inquiries or comments.
Thank you!
Dear Designers, i have taken your comments into consideration and guaranteed the payment.
B2b, banks, financial institutions, large companies
Real Estate

```html
<!DOCTYPE html>
<html lang="en">
<head>
<meta charset="utf-8">
<title>Velmo Real Estate Broker – Tri-fold Brochure</title>
<link rel="stylesheet" href="https://fonts.googleapis.com/css2?family=PT+Sans:wght@400;700&family=Roboto+Condensed:wght@700&display=swap">
<style>
  :root{
    --bg:#141414;
    --green:#17a04b;
    --red:#c41f30;
    --ink:#333;
    --paper:#fff;
    --grey:#e9e9e9;
    --client:#1d3a6b;
  }
  *{box-sizing:border-box;margin:0;padding:0}
  html,body{width:1200px;height:512px;overflow:hidden;background:var(--bg)}
  body{position:relative;font-family:"PT Sans",sans-serif;color:var(--ink)}
  .spread{position:absolute;top:42px;width:538px;height:417px;display:flex}
  .spread--outside{left:40px}
  .spread--inside{left:621px}
  .panel{position:relative;width:180px;height:100%;overflow:hidden;background:var(--paper)}
  .panel--green{background:var(--green);color:#fff}
  .body-text{font-size:6.6px;line-height:1.32;text-align:justify}
  .body-text p+p{margin-top:7px}
  .photo{position:absolute;left:0;width:100%}
  .brand-title{font-family:"Roboto Condensed",sans-serif;font-weight:700;text-transform:uppercase;letter-spacing:-.2px}
  .wordmark{display:flex;align-items:center;gap:5px;font-family:"Roboto Condensed",sans-serif;font-weight:700;letter-spacing:1px}
  .wordmark i{display:block;width:10px;height:10px}

  /* outside: intro panel */
  .intro__top{position:absolute;top:0;left:0;width:100%;height:113px;background:var(--green);color:#fff;padding:13px 12px 0 12px}
  .intro__bottom{position:absolute;top:246px;left:0;width:100%;padding:0 12px}
  .red-rule{position:absolute;left:0;width:100%;height:4px;background:var(--red)}

  /* outside: contact panel */
  .contact{text-align:center}
  .contact .wordmark{position:absolute;top:58px;left:0;width:100%;justify-content:center;font-size:22px;color:#fff}
  .contact .wordmark i{background:#fff}
  .contact .brand-title{position:absolute;top:101px;width:100%;font-size:13px}
  .contact h3{position:absolute;top:137px;width:100%;font-size:12.5px;font-weight:700}
  .contact__lines{position:absolute;top:163px;width:100%;font-size:6.8px;line-height:1.45}
  .contact__lines p+p{margin-top:8px}
  .contact h4{position:absolute;top:300px;width:100%;font-size:12px;font-weight:700}
  .clients{position:absolute;top:328px;left:0;width:100%;height:89px;background:var(--paper);display:grid;grid-template-columns:1fr 1fr;align-items:center;padding:6px 6px}
  .client{display:flex;align-items:center;justify-content:center;gap:4px;font-size:9.5px;font-weight:700;color:var(--client)}
  .client i{display:block;width:9px;height:9px;background:var(--client)}

  /* outside: cover panel */
  .cover__sky{position:absolute;top:0;left:0;width:100%;height:126px;background:linear-gradient(#fff,#f1f1f1)}
  .cover .wordmark{position:absolute;top:28px;left:0;width:100%;justify-content:center;font-size:24px;color:var(--green)}
  .cover .wordmark i{background:var(--red)}
  .cover .brand-title{position:absolute;top:75px;width:100%;text-align:center;font-size:14px;color:#222}
  .cover__band{position:absolute;top:322px;left:0;width:100%;height:95px;background:var(--red);color:#fff;text-align:center;padding-top:16px}
  .cover__band p{font-size:9.4px;font-weight:700;line-height:1.4}
  .cover__band a{display:block;margin-top:13px;font-size:12px;line-height:1.2;font-weight:700;color:#fff;text-decoration:none}

  /* inside */
  .section-title{font-family:"Roboto Condensed",sans-serif;font-weight:700;font-size:12.5px;text-transform:uppercase;padding-bottom:4px;border-bottom:2px solid var(--red)}
  .services{padding:18px 10px 0 9px}
  .services .section-title{color:var(--red)}
  .ticks{list-style:none;margin-top:14px;font-size:7px;line-height:1.25}
  .ticks li{display:flex;gap:7px;margin-bottom:7px}
  .ticks svg{flex:none;margin-top:1px}
  .services__note{position:absolute;top:345px;left:10px;right:10px}
  .leadership__photo{position:absolute;top:8px;left:8px;width:164px;height:122px}
  .leadership__body{position:absolute;top:139px;left:0;width:100%;height:278px;background:var(--green);color:#fff;padding:8px 10px 0 10px}
  .leadership__body .section-title{border-bottom-color:#fff;color:#fff;margin-bottom:8px}
  .leadership__body .body-text p+p{margin-top:8px}
  .why{padding:18px 10px 0 11px}
  .why .section-title{color:var(--red);margin-bottom:13px}
  .why .section-title.about{margin-top:18px}
</style>
</head>
<body>

<section class="spread spread--outside">
  <article class="panel intro">
    <div class="intro__top body-text">
      <p>Velmo Real Estate Broker was formed in 2005 to tap the opportunities provided by a fast developing real estate sector in UAE and Dubai in particular. We have properties in Dubai and Abu Dhabi under our total management. From leasing properties to maintenance and upkeep, fire safety requirements, coordination with Civil Defense, Real Estate Regulatory Agency (RERA) and Municipality we handle every aspect of property management.</p>
    </div>
    <div class="photo" style="top:113px;height:113px;background:linear-gradient(120deg,#7a8a99,#d9dde2 55%,#556677)" role="img" aria-label="Photo of a business team meeting around a table"></div>
    <div class="red-rule" style="top:226px"></div>
    <div class="intro__bottom body-text">
      <p>The Real Estate and Property Management team is led by the Director who has massive experience of Real Estate and Property Management. Our staff also has dynamic experience of the current market of Real Estate. We actively seek to engage with our clients to ensure that the right services are matched to their individual and changing needs.</p>
      <p>We bring together a wealth of knowledge and experience to offer asset management, property management and consultancy advice on any asset class, portfolio or holding, however big or small.</p>
    </div>
  </article>

  <article class="panel panel--green contact">
    <div class="wordmark"><i></i>VELMO</div>
    <h2 class="brand-title">Velmo Real Estate Broker</h2>
    <h3>Contact Info</h3>
    <div class="contact__lines">
      <p>210 Al Noor Tower Qusais Harbour Street,<br>OPP Palm Training Centre</p>
      <p>Call: 045107318</p>
      <p>Fax: 045107392</p>
      <p>E-mail: info@velmo-grp.ae</p>
    </div>
    <h4>Our Clients</h4>
    <div class="clients">
      <div class="client"><i></i>Sahra Bank</div>
      <div class="client">Qamar Finance</div>
      <div class="client">Northgate Bank</div>
      <div class="client"><i></i>Dunes National</div>
    </div>
  </article>

  <article class="panel cover">
    <div class="cover__sky"></div>
    <div class="wordmark"><i></i>VELMO</div>
    <h1 class="brand-title">Velmo Real Estate Broker</h1>
    <div class="red-rule" style="top:122px"></div>
    <div class="photo" style="top:126px;height:196px;background:linear-gradient(160deg,#e6e6e6,#b9b2a6 45%,#7d8a96)" role="img" aria-label="Illustration of a family house with a grey roof"></div>
    <div class="cover__band">
      <p>We aim to become a creative company<br>that grows continuously throughout<br>the future.</p>
      <a href="#">www.velmo-grp.ae</a>
    </div>
  </article>
</section>

<section class="spread spread--inside">
  <article class="panel services">
    <h2 class="section-title">Our Services Includes</h2>
    <ul class="ticks">
      <li><svg width="6" height="6" viewBox="0 0 6 6"><path d="M.5 3.2 2.3 5 5.5.8" fill="none" stroke="#333" stroke-width="1.2"/></svg>Letting properties</li>
      <li><svg width="6" height="6" viewBox="0 0 6 6"><path d="M.5 3.2 2.3 5 5.5.8" fill="none" stroke="#333" stroke-width="1.2"/></svg>Maintenance and upkeep</li>
      <li><svg width="6" height="6" viewBox="0 0 6 6"><path d="M.5 3.2 2.3 5 5.5.8" fill="none" stroke="#333" stroke-width="1.2"/></svg>Coordination with Dubai Land Department (RERA)</li>
      <li><svg width="6" height="6" viewBox="0 0 6 6"><path d="M.5 3.2 2.3 5 5.5.8" fill="none" stroke="#333" stroke-width="1.2"/></svg>Coordination with Dubai Civil Defense</li>
      <li><svg width="6" height="6" viewBox="0 0 6 6"><path d="M.5 3.2 2.3 5 5.5.8" fill="none" stroke="#333" stroke-width="1.2"/></svg>Coordination with Municipality guidelines and regulations</li>
      <li><svg width="6" height="6" viewBox="0 0 6 6"><path d="M.5 3.2 2.3 5 5.5.8" fill="none" stroke="#333" stroke-width="1.2"/></svg>Other services required for every aspect of property management.</li>
    </ul>
    <div class="photo" style="top:190px;left:9px;width:160px;height:138px;border:1px solid #ccc;background:linear-gradient(135deg,#cfd3cf,#e9e4dc 50%,#b34a3b)" role="img" aria-label="Photo of a model house on banknotes beside a calculator"></div>
    <p class="services__note body-text">We aim to fill the market gap in terms of potential investment opportunities which have been raised due to Dubai's winning bid to host Expo 2020. We utilize our diverse experience to exceed existing industry benchmarks through consistent follow up and real estate advisory approach.</p>
  </article>

  <article class="panel leadership" style="background:var(--grey)">
    <div class="leadership__photo" style="background:linear-gradient(#f4f4f4,#c9c2b8)" role="img" aria-label="Portrait of the company founder"></div>
    <div class="leadership__body">
      <h2 class="section-title">Our Leadership</h2>
      <div class="body-text">
        <p>Mr. Omar Saeed Al Harbi is the founder of the company. Member of The Guild of Chartered Public Accountants International (GCPAI) as well as awarded with Degree of Associate Professor for Property management by the Hollins Ridge University, New York, USA.</p>
        <p>He has worked in the financial services, banking and consulting industry for close to two decades and is recognized as one of the leading authorities on Accounting and Banking Expert as well as Arbitration. He has immense knowledge of UAE Banking industry and regional business markets as well as every facet of Real Estate activity. He started his banking career in 1987 with Creek National Bank.</p>
        <p>He has been Head of Retail Banking at the Head Office in Dubai. After merger of the bank with Gulfway Bank International in 2009 he was appointed as the General Manager, Properties at Dunes National Bank, the new entity and is currently looking after the properties of the group that extended over the whole U.A.E. He is also a member of the Board for Islamic Banking of the bank.</p>
      </div>
    </div>
  </article>

  <article class="panel why">
    <h2 class="section-title">Why Velmo Group?</h2>
    <div class="body-text">
      <p>To ensure customer satisfaction, Velmo Group encourages "management by all employees," continuously enhancing our capability on the work load and our power to achieve</p>
      <p>We at Velmo Group strive to deliver services that delight our customers. The "Customer-First" Principle is our top priority. Satisfying customers requires that we have strong capabilities on the Team board — a necessary starting point for any work, especially in fields like CONSULTATION, ACCOUNTS AND LEGAL — as well as the "power to achieve," which permits us to accomplish worthy goals without fail.</p>
    </div>
    <h2 class="section-title about">About Velmo Group</h2>
    <div class="body-text">
      <p>Velmo Group is an alliance of talented Certified Public Accountants, Arbiters and Financial Experts joined together to provide the UAE business community with value added Advisory and Accounting solutions tailored to its needs. The principles on which the group is based are responsibility and integrity.</p>
      <p>With 22 years of combined business experience, Our Director is a Certified Public Accountant with distinguished qualifications and our staff has extensive experience in the areas of External/Internal Audit, Management Accounting, Risk Management, Financial Restructuring, and Corporate Governance.</p>
    </div>
  </article>
</section>

</body>
</html>
```